依頼詳細
社屋新築工事に伴い、独立看板の設置が必要となりました。
ロゴを含む看板全体のデザインを希望します。
サイズにつきまして、配置図の情報をもとにご提案いただきたいです。

■看板についての要望
・杉浦製作所のイメージに相応しい看板
・本社屋に来客した人に分かる看板
・杉浦製作所のイメージを伝えるような看板
・配置に関して駐車場に車両を駐車してもわかる看板

■サイズ
看板の大きさは、タテ・ヨコは、5.0×0.9~1.2m又は0.9~1.2×5.0mでお願いします。
高さは最大6mくらいでお願いします。
ヨコ長の場合は車両より上に設置予定。
※配置図を提供いたします。こちら考慮の上、デザイン制作をお願いいたします。

■提供資料
・建物 パース(完成イメージ)
・配置図
・ロゴ画像(HPより利用ください)

その他不明点は、やり取りの中で相談しながら進めさせてください。
記載項目
会社名「株式会社 霧丘製作所」/電話番号「TEL:0493-61-2740」/ロゴ「Sk」のマークのもの 看板の表示項目で会社名以外はデザイナーさんのイメージで判断下さい。
希望イメージ
シンプル 複雑
単色 カラフル
暗い 明るい
日常 高級
遊び心 厳粛
未来的 伝統的
女性的 男性的
希望する色
納品ファイル
• 高解像度JPG (.jpg)
• PNG形式 (.png)
補足説明
■ 選んだ理由

施主様に選考頂きました。
シンプルで目立つもので選びましたと話をされていました。

■ 提案者全員のお礼・コメント

たくさんのすてきなデザインを作成頂きましてありがとうございました。
今回はじめてツクリバを利用しました。
色々とシステムが呑み込めず、上手く出来ませんでしたが、
また、今後もこのうような案件がありましたら利用しようと思います。
今回参加頂きましたツクリバーの皆様、ありがとうございました。

```html
<!DOCTYPE html>
<html lang="ja">
<head>
<meta charset="utf-8">
<title>看板デザイン – 株式会社 霧丘製作所</title>
<link href="https://fonts.googleapis.com/css2?family=Noto+Serif+JP:wght@600&family=Noto+Sans+JP:wght@400;500&family=Montserrat:wght@500&display=swap" rel="stylesheet">
<style>
  :root{
    --paper:#ffffff;
    --ink:#1a1a1a;
    --sky-top:#1f4f8f;
    --sky-mid:#5f8fc4;
    --sky-low:#c9d9e8;
    --brand:#e0533a;
    --text-grey:#4a4a4a;
    --copy:#ffffff;
  }
  *{margin:0;padding:0;box-sizing:border-box}
  html,body{width:805px;height:1200px;overflow:hidden;background:var(--paper)}
  .sheet{position:relative;width:805px;height:1200px;background:var(--paper);font-family:"Noto Sans JP",sans-serif;color:var(--ink)}
  .sheet-title{position:absolute;left:268px;top:62px;font-size:13px;font-weight:500;letter-spacing:.02em}
  .signboard{position:absolute;left:268px;top:90px;width:270px;height:1020px;border:1px solid #cfcfcf;background:var(--paper);overflow:hidden}
  .sign-photo{position:absolute;left:0;top:0;width:100%;height:700px;
    background:
      radial-gradient(circle at 22% 10%, rgba(255,255,255,.95) 0, rgba(255,255,255,.5) 8%, rgba(255,255,255,0) 26%),
      linear-gradient(180deg,var(--sky-top) 0%,var(--sky-mid) 45%,var(--sky-low) 100%)}
  .sign-copy{position:absolute;left:148px;top:26px;writing-mode:vertical-rl;font-family:"Noto Serif JP",serif;font-weight:600;font-size:33px;line-height:1;letter-spacing:.1em;color:var(--copy);text-shadow:0 0 6px rgba(0,40,90,.35)}
  .sign-brand{position:absolute;left:0;top:700px;width:100%;height:320px;text-align:center}
  .brand-dot{width:98px;height:98px;border-radius:50%;background:var(--brand);margin:42px auto 0}
  .brand-name{margin-top:22px;font-family:"Montserrat",sans-serif;font-weight:500;font-size:30px;letter-spacing:.06em;color:var(--text-grey)}
  .company-name{margin-top:16px;font-size:17px;color:var(--text-grey);letter-spacing:.04em;word-spacing:.6em}
  .company-tel{margin-top:8px;font-size:17px;color:var(--text-grey);letter-spacing:.04em;display:flex;justify-content:center;align-items:center;gap:4px}
  .title-block{position:absolute;left:22px;right:22px;top:1140px;height:42px;border-top:3px solid var(--ink);border-bottom:3px solid var(--ink);display:grid;grid-template-columns:138px 143px 309px 1fr}
  .title-block .cell{border-left:1px solid var(--ink);font-size:8px;padding:2px 4px}
  .title-block .cell.mark{border-left:none;background:var(--ink)}
</style>
</head>
<body>
<div class="sheet">
  <p class="sheet-title">■看板デザイン (W1200×H5000)</p>

  <div class="signboard">
    <div class="sign-photo" role="img" aria-label="青空に向かって紙飛行機を飛ばす人々の手の写真"></div>
    <p class="sign-copy">ひとりひとりが笑顔で生きる未来へ。</p>

    <div class="sign-brand">
      <div class="brand-dot"></div>
      <p class="brand-name">KIRIOKA</p>
      <p class="company-name">株式会社 霧丘製作所</p>
      <p class="company-tel">
        <svg width="16" height="16" viewBox="0 0 24 24" aria-hidden="true"><path fill="none" stroke="#4a4a4a" stroke-width="2" d="M6.6 3.5l3 3.2-2 2.3a13 13 0 0 0 7.4 7.4l2.3-2 3.2 3-2.4 3.1C10.4 19.8 4.2 13.6 3.5 5.9z"/></svg>
        0000-12-3456
      </p>
    </div>
  </div>

  <div class="title-block">
    <div class="cell mark"></div>
    <div class="cell">Date</div>
    <div class="cell">Customer Name</div>
    <div class="cell">Designer</div>
  </div>
</div>
</body>
</html>
```